Photography Studio Prep Guide Design Needed

I have a prep guide I send to all parents who book a session - It is outdated and ugly. I want a gorgeous, clean, modern upscale look for the brochure I send.

I already have the text and can provide photos for the final design. I want the cover to be clean and upscale and modern, with a happy feel.

Target Market(s)

My clients for an upscale Newborn Photography Studio

Requirements
Must have
• space for my photos, an upscale clean feel
Nice to have
• I love color, but don't want the brochure to look busy. I love cream, white, pale pink.

```html
<!DOCTYPE html>
<html lang="en">
<head>
<meta charset="UTF-8">
<title>Parent Instructions &amp; Preparations</title>
<link href="https://fonts.googleapis.com/css2?family=Pinyon+Script&family=Playfair+Display:ital,wght@1,600&display=swap" rel="stylesheet">
<style>
  :root {
    --blush: #efb8bb;
    --rose: #e8a4aa;
    --rose-deep: #dc9aa0;
    --paper: #ffffff;
    --lawn-dark: #2f5a2c;
    --lawn-mid: #3f7a39;
    --lawn-light: #4d8a45;
    --stitch: #a9aaa6;
    --ink-light: #ffffff;
  }
  * { margin: 0; padding: 0; box-sizing: border-box; }
  html, body { width: 1183px; height: 1200px; overflow: hidden; background: var(--blush); }
  .guide-page { position: relative; width: 1183px; height: 1200px; background: var(--blush); }
  .page-frame {
    position: absolute; left: 16px; top: 22px; width: 1150px; height: 1160px;
    background: var(--paper); border-radius: 12px;
  }
  .lawn-backdrop {
    position: absolute; left: 21px; top: 27px; width: 1141px; height: 1151px;
    border-radius: 8px;
    background: radial-gradient(ellipse at 40% 35%, var(--lawn-light), var(--lawn-mid) 55%, var(--lawn-dark));
  }
  .stitch-border {
    position: absolute; left: 35px; top: 46px; width: 1114px; height: 1120px;
    border: 3px dashed var(--stitch); border-radius: 6px;
  }
  .guide-title {
    position: absolute; left: 0; top: 60px; width: 1192px; text-align: center;
    font-family: "Pinyon Script", cursive; font-size: 52px; color: var(--rose);
    font-weight: 400; line-height: 1.2;
  }
  .copy {
    position: absolute; text-align: center; color: var(--ink-light);
    font-family: "Playfair Display", serif; font-style: italic; font-weight: 600;
    font-size: 19.5px; line-height: 26.4px; text-shadow: 0 1px 2px rgba(0,0,0,.35);
  }
  .copy-left { left: 58px; top: 137px; width: 545px; }
  .copy-right { left: 598px; top: 698px; width: 545px; }
  .section-heading {
    display: inline-block; font-family: "Pinyon Script", cursive; font-style: normal;
    font-weight: 400; font-size: 31px; line-height: 36px; color: var(--rose);
    border-bottom: 2px solid var(--rose); text-shadow: none; margin: 2px 0 4px;
  }
  .feeding-heading { position: absolute; left: 598px; top: 654px; width: 545px; text-align: center; }
  .feeding-heading .section-heading { margin: 0; }
  .photo-slot {
    position: absolute; background: var(--paper); border-radius: 8px;
  }
  .photo-slot::after {
    content: ""; position: absolute; inset: 12px;
    border: 1.5px dashed var(--rose-deep);
  }
  .photo-slot-left { left: 62px; top: 654px; width: 482px; height: 480px; }
  .photo-slot-right { left: 642px; top: 164px; width: 482px; height: 478px; }
  .bow-ornament {
    position: absolute; width: 108px; height: 110px; z-index: 2;
    background: linear-gradient(180deg, var(--rose), var(--rose-deep));
    border-radius: 40px 40px 10px 10px;
  }
  .bow-left { left: 250px; top: 634px; }
  .bow-right { left: 830px; top: 144px; }
</style>
</head>
<body>
<div class="guide-page">
  <div class="page-frame"></div>
  <div class="lawn-backdrop" role="img" aria-label="Green grass texture background"></div>
  <div class="stitch-border"></div>

  <h1 class="guide-title">Parent Instructions &amp; Preparations</h1>

  <div class="copy copy-left">
    <p>Congratulations on expecting a baby! Here are my<br>instructions to ensure a successful newborn photog-<br>raphy session. Please follow these instructions as<br>closely as possible.</p>
    <h2 class="section-heading">1.Nursing</h2>
    <p>If you are nursing, please avoid eating anything<br>spicy (hot sauce, hot peppers, curry, etc.) that<br>might upset baby’s tummy for 24 hours preceding<br>your scheduled session.<br>Please if you are breastfeeding do NOT drink caf-<br>feine or coffee before your session – I know<br>this is hard but baby will be wired if you have caf-<br>feine.<br>If you notice baby has a lot of gas after feedings<br>please check with your pediatrician and bring<br>gas drops (TummyEase or other brand) to your session.<br>The most common reason a baby will not<br>settle for a session is gas pressure/discomfort.</p>
  </div>

  <div class="photo-slot photo-slot-left" role="img" aria-label="Space for a newborn session photo"></div>
  <div class="bow-ornament bow-left" role="img" aria-label="Pale pink ribbon bow decoration"></div>

  <div class="photo-slot photo-slot-right" role="img" aria-label="Space for a newborn session photo"></div>
  <div class="bow-ornament bow-right" role="img" aria-label="Pale pink ribbon bow decoration"></div>

  <div class="feeding-heading"><h2 class="section-heading">2.Feeding</h2></div>
  <div class="copy copy-right">
    <p>Feed the baby as much as possible in the 24 hours<br>preceding your session – this will help<br>minimize the amount baby needs to feed during the<br>session, and will help baby sleep as long<br>and as soundly as possible. Feed baby 2-3 hours<br>before your session and not again until you<br>arrive. This feeding is planned in your session time<br>and it’s not rushed.<br>Please bring an extra bottle of formula or breast-<br>milk to the session if possible – sometimes a<br>small amount of milk in a bottle can quickly soothe<br>a baby back to sleep without requiring a full<br>feeding. I will respect your wishes if you choose not<br>to use a bottle, but please understand we<br>may have to pass on some poses if baby will not<br>settle in position, and I cannot use a bottle to<br>soothe them into the pose.</p>
  </div>
</div>
</body>
</html>
```